Pale Lanterns Old Lane Walk Poster Design

We need an A4 sized poster to promote our weekly true crime tours. This poster will be posted onto community noticeboards.
Lots of information and images can be viewed at the following links:-
www.palelanterns.com.au
www.palelanterns.com.au/bookings/
https://www.facebook.com/palelanternsoldlane/
https://www.examplereviews.com.au/Attraction_Review-g000000-d00000000-Reviews-Pale_Lanterns-Newcastle_Greater_Newcastle_New_South_Wales.html
There are also a number of images for possible use at the following link - we are open to intepretation:-
http://palelanterns.com.au/tour-photographs/
The font on our website is "SpecialElite" so we would like to continue using that font type.
Target Market(s)
Adults 25-65.
Font styles to use
Other font styles liked:
- Special Elite
Colors
Designer to choose colors to be used in the design.
Look and feel
Each slider illustrates characteristics of the customer's brand and the style your logo design should communicate.

```html
<!DOCTYPE html>
<html lang="en">
<head>
<meta charset="utf-8">
<title>Pale Lanterns Old Lane Walk Poster</title>
<link href="https://fonts.googleapis.com/css2?family=Special+Elite&family=Courier+Prime:wght@400;700&display=swap" rel="stylesheet">
<style>
  :root {
    --backdrop: #6a6a6a;
    --paper-light: #ece2cc;
    --paper-mid: #dccdb0;
    --paper-dark: #bfa985;
    --band-red: #6e0000;
    --band-deep: #3c0000;
    --ink: #111111;
    --ink-grey: #4a4a4a;
    --title-light: #9a9a9a;
    --accent-red: #e4161b;
    --label-red: #7e0c0c;
    --star: #f7b500;
  }
  * { margin: 0; padding: 0; box-sizing: border-box; }
  html, body { width: 1000px; height: 1200px; overflow: hidden; }
  body { background: var(--backdrop); position: relative; font-family: "Special Elite", "Courier New", monospace; }

  .poster {
    position: absolute; left: 125px; top: 75px; width: 745px; height: 1055px;
    background: radial-gradient(ellipse at 50% 40%, var(--paper-light) 0%, var(--paper-mid) 60%, var(--paper-dark) 100%);
    overflow: hidden; color: var(--ink);
  }
  .street-band {
    position: absolute; left: 245px; top: 0; width: 252px; height: 100%;
    background: linear-gradient(180deg, var(--band-red) 0%, #8a0b0b 30%, #7a0505 55%, var(--band-deep) 75%, #4a0202 100%);
  }
  .brand-mark {
    position: absolute; left: 245px; width: 252px; top: 48px;
    text-align: center; font-size: 26px; color: var(--ink); letter-spacing: 1px;
  }
  .review { position: absolute; top: 113px; font-size: 17px; line-height: 20px; }
  .review--left { right: 512px; text-align: right; }
  .review--right { left: 513px; text-align: left; }
  .stars { display: flex; gap: 3px; margin-bottom: 8px; }
  .review--left .stars { justify-content: flex-end; }
  .stars svg { width: 23px; height: 22px; fill: var(--star); }
  .review .source { font-size: 15px; }

  .title-main {
    position: absolute; left: 0; width: 100%; top: 238px; text-align: center;
    font-size: 200px; line-height: 190px; letter-spacing: 8px; color: var(--ink-grey);
  }
  .title-sub {
    position: absolute; left: 0; width: 100%; top: 470px; text-align: center;
    font-size: 94px; line-height: 100px; letter-spacing: 8px; color: var(--ink-grey);
  }
  .title-main .lit, .title-sub .lit { color: var(--title-light); }

  .tagline { position: absolute; font-family: "Courier Prime", "Courier New", monospace; font-weight: 700; font-size: 26px; letter-spacing: 2px; white-space: nowrap; }
  .tagline .red { color: var(--accent-red); }
  .tagline--one { left: 98px; top: 593px; }
  .tagline--two { left: 378px; top: 630px; }
  .tagline--three { left: 55px; top: 672px; font-size: 22px; }

  .offer { position: absolute; font-family: "Courier Prime", "Courier New", monospace; font-weight: 700; font-size: 22px; line-height: 30px; letter-spacing: 2px; color: var(--label-red); }
  .offer--tour { right: 505px; top: 753px; text-align: right; }
  .offer--confess { left: 505px; top: 783px; }

  .book-call { position: absolute; left: 255px; top: 750px; width: 235px; height: 112px; }
  .book-call .hands { position: absolute; inset: 0; background: linear-gradient(135deg, #2a0000 0%, #4d1a1a 50%, #2a0000 100%); opacity: .55; border-radius: 4px; }
  .book-call .label { position: absolute; left: 0; right: 0; top: 32px; text-align: center; font-size: 42px; color: #8e1a1a; letter-spacing: 2px; }

  .contact { position: absolute; top: 915px; width: 200px; text-align: center; font-size: 19px; line-height: 21px; }
  .contact svg { display: block; margin: 0 auto 14px; width: 46px; height: 46px; fill: var(--ink); }
  .contact--phone { left: 20px; }
  .contact--mail { left: 271px; }
  .contact--web { left: 527px; }
  .contact--phone p { margin-top: 18px; }
</style>
</head>
<body>
<main class="poster">
  <div class="street-band" role="img" aria-label="Dim red-toned photograph of an old city street at night with a lone walker"></div>

  <div class="brand-mark">Pale Lanterns</div>

  <div class="review review--left">
    <div class="stars">
      <svg viewBox="0 0 24 24"><path d="M12 1l3.2 7 7.6.7-5.7 5 1.7 7.5L12 17.3 5.2 21.2l1.7-7.5-5.7-5 7.6-.7z"/></svg>
      <svg viewBox="0 0 24 24"><path d="M12 1l3.2 7 7.6.7-5.7 5 1.7 7.5L12 17.3 5.2 21.2l1.7-7.5-5.7-5 7.6-.7z"/></svg>
      <svg viewBox="0 0 24 24"><path d="M12 1l3.2 7 7.6.7-5.7 5 1.7 7.5L12 17.3 5.2 21.2l1.7-7.5-5.7-5 7.6-.7z"/></svg>
      <svg viewBox="0 0 24 24"><path d="M12 1l3.2 7 7.6.7-5.7 5 1.7 7.5L12 17.3 5.2 21.2l1.7-7.5-5.7-5 7.6-.7z"/></svg>
      <svg viewBox="0 0 24 24"><path d="M12 1l3.2 7 7.6.7-5.7 5 1.7 7.5L12 17.3 5.2 21.2l1.7-7.5-5.7-5 7.6-.7z"/></svg>
    </div>
    <p>Fabulous addition<br>to New Castle</p>
    <p class="source">-from ReviewHub</p>
  </div>

  <div class="review review--right">
    <div class="stars">
      <svg viewBox="0 0 24 24"><path d="M12 1l3.2 7 7.6.7-5.7 5 1.7 7.5L12 17.3 5.2 21.2l1.7-7.5-5.7-5 7.6-.7z"/></svg>
      <svg viewBox="0 0 24 24"><path d="M12 1l3.2 7 7.6.7-5.7 5 1.7 7.5L12 17.3 5.2 21.2l1.7-7.5-5.7-5 7.6-.7z"/></svg>
      <svg viewBox="0 0 24 24"><path d="M12 1l3.2 7 7.6.7-5.7 5 1.7 7.5L12 17.3 5.2 21.2l1.7-7.5-5.7-5 7.6-.7z"/></svg>
      <svg viewBox="0 0 24 24"><path d="M12 1l3.2 7 7.6.7-5.7 5 1.7 7.5L12 17.3 5.2 21.2l1.7-7.5-5.7-5 7.6-.7z"/></svg>
      <svg viewBox="0 0 24 24"><path d="M12 1l3.2 7 7.6.7-5.7 5 1.7 7.5L12 17.3 5.2 21.2l1.7-7.5-5.7-5 7.6-.7z"/></svg>
    </div>
    <p>History comes<br>arrive</p>
    <p class="source">-Marion K</p>
  </div>

  <h1 class="title-main">P<span class="lit">AL</span>E</h1>
  <h2 class="title-sub">L<span class="lit">AN</span>T<span class="lit">E</span>R<span class="lit">N</span>S</h2>

  <p class="tagline tagline--one">..revisi<span class="red">t the scenes</span></p>
  <p class="tagline tagline--two"><span class="red">of the</span> crimes..</p>
  <p class="tagline tagline--three">take a walk on the dark side</p>

  <p class="offer offer--tour">TRUE CRIME<br>TOUR</p>
  <div class="book-call">
    <div class="hands" role="img" aria-label="Engraved illustration of two pointing hands"></div>
    <span class="label">BOOK</span>
  </div>
  <p class="offer offer--confess">CONFESSIONS<br>OF A<br>SERIAL KILLER</p>

  <div class="contact contact--phone">
    <svg viewBox="0 0 24 24"><path d="M6.6 10.8c1.4 2.8 3.8 5.1 6.6 6.6l2.2-2.2c.3-.3.7-.4 1-.2 1.1.4 2.3.6 3.6.6.6 0 1 .4 1 1V20c0 .6-.4 1-1 1C10.6 21 3 13.4 3 4c0-.6.4-1 1-1h3.5c.6 0 1 .4 1 1 0 1.3.2 2.5.6 3.6.1.3 0 .7-.2 1z"/></svg>
    <p>0400 000 123</p>
  </div>
  <div class="contact contact--mail">
    <svg viewBox="0 0 24 24"><path d="M2 5h20v14H2z M3.5 6.5v.3L12 13l8.5-6.2v-.3z M3.5 8.6v8.9h17V8.6L12 14.8z" fill-rule="evenodd"/></svg>
    <p>info<br>@palelanterns<br>.com.au</p>
  </div>
  <div class="contact contact--web">
    <svg viewBox="0 0 24 24" fill="none" stroke="#111" stroke-width="1.6"><circle cx="12" cy="12" r="10"/><ellipse cx="12" cy="12" rx="4.5" ry="10"/><path d="M2 12h20M12 2v20M4 6.5h16M4 17.5h16"/></svg>
    <p>www<br>.palelanterns<br>.com.au</p>
  </div>
</main>
</body>
</html>
```